Announcement Card

This will be an announcement card mailed to clients as a postcard. The text should be oriented book fashion (not landscape).

Text is:

DEREK T. HOLLOWAN

is pleased to announce
he is joining

BRIARCREST LAW GROUP

as a founding partner

[PHONE, ADDRESS, EMAIL]

Industry/Entity Type

Fashion

```html
<!DOCTYPE html>
<html lang="en">
<head>
<meta charset="utf-8">
<title>Announcement Card – Derek T. Hollowan</title>
<link rel="stylesheet" href="https://fonts.googleapis.com/css2?family=Cinzel:wght@400;600&family=Tinos:ital@1&display=swap">
<style>
  :root {
    --backdrop: #e9e9e9;
    --card-white: #ffffff;
    --brand-red: #8f2222;
    --brand-red-dark: #6e1515;
    --brand-red-light: #a52a2a;
    --silver: #c4c4c6;
    --silver-dark: #8d8d90;
    --text-grey: #6f6f6f;
    --photo-warm: #c9ad7e;
    --photo-cool: #5a7aa6;
  }
  * { margin: 0; padding: 0; box-sizing: border-box; }
  html, body {
    width: 1200px; height: 1000px; overflow: hidden;
    background: var(--backdrop);
  }
  .card {
    position: absolute; left: 322px; top: 133px;
    width: 554px; height: 720px;
    background: var(--card-white);
    overflow: hidden;
  }
  .card-bands { position: absolute; inset: 0; }
  .portrait-frame {
    position: absolute; left: 202px; top: 55px;
    width: 152px; height: 179px;
    background: #fff;
    border: 1px solid #dcdcdc;
    box-shadow: 2px 3px 3px rgba(0,0,0,0.12);
  }
  .portrait {
    position: absolute; left: 7px; top: 7px;
    width: 137px; height: 162px;
    background: linear-gradient(180deg, var(--photo-warm) 0%, #b89a70 45%, var(--photo-cool) 100%);
  }
  .copy {
    position: absolute; left: 0; width: 100%;
    text-align: center;
  }
  .name {
    top: 266px;
    font-family: 'Cinzel', serif; font-weight: 600;
    font-size: 40px; letter-spacing: 1px;
    color: var(--brand-red);
  }
  .lead, .closing {
    font-family: 'Tinos', serif; font-style: italic;
    font-size: 22px; color: var(--text-grey);
  }
  .lead { top: 330px; }
  .closing { top: 490px; }
  .firm-name {
    top: 431px;
    font-family: 'Cinzel', serif; font-weight: 600;
    font-size: 22px; letter-spacing: 0.5px;
    color: var(--brand-red);
  }
  .contact {
    top: 558px;
    font-family: 'Cinzel', serif; font-weight: 400;
    font-size: 14px; line-height: 18px;
    color: var(--brand-red);
  }
  .contact p { margin-bottom: 8px; }
  .contact .label { font-weight: 600; }
</style>
</head>
<body>
  <main class="card">
    <svg class="card-bands" width="554" height="720" viewBox="0 0 554 720" aria-hidden="true">
      <defs>
        <linearGradient id="redBand" x1="0" x2="1" y1="0" y2="0">
          <stop offset="0" stop-color="var(--brand-red-dark)"/>
          <stop offset="0.45" stop-color="var(--brand-red-light)"/>
          <stop offset="1" stop-color="var(--brand-red-dark)"/>
        </linearGradient>
        <linearGradient id="silverEdge" x1="0" x2="1" y1="0" y2="0">
          <stop offset="0" stop-color="var(--silver-dark)"/>
          <stop offset="0.5" stop-color="#eeeeee"/>
          <stop offset="1" stop-color="var(--silver-dark)"/>
        </linearGradient>
      </defs>
      <!-- top band -->
      <path d="M0,0 H554 V92 C380,36 150,86 0,214 Z" fill="url(#redBand)"/>
      <path d="M0,224 C150,94 380,48 554,104" fill="none" stroke="url(#silverEdge)" stroke-width="8"/>
      <!-- bottom band -->
      <path d="M0,620 C150,708 380,716 554,608 V720 H0 Z" fill="url(#redBand)"/>
      <path d="M0,612 C150,700 380,708 554,600" fill="none" stroke="url(#silverEdge)" stroke-width="8"/>
    </svg>

    <div class="portrait-frame">
      <div class="portrait" role="img" aria-label="Portrait photograph of Derek T. Hollowan"></div>
    </div>

    <h1 class="copy name">DEREK T. HOLLOWAN</h1>
    <p class="copy lead">is pleased to announce he is joining</p>
    <p class="copy firm-name">BRIARCREST LAW GROUP</p>
    <p class="copy closing">as a founding partner.</p>

    <address class="copy contact" style="font-style:normal">
      <p><span class="label">P:</span> +1 617 555 0142</p>
      <p><span class="label">A:</span> 48 Harbor Lane, Suite 310<br>BOSTON, MA 02110</p>
      <p><span class="label">E:</span> derekhollowan@briarcrest.com</p>
    </address>
  </main>
</body>
</html>
```